Bluewater Getaways KT needs a new Website

We have an old website that is just that - old. We need a fresh website that is professional graphic designed that has the following features.
1. Can be updated by ourselves in some areas.
2. Has a shopping cart.
3. Has links to download PDF files
4. Has links to other pages in the website
5. Includes social media links
6. Has a client log-in area
Full details in brief provided.

SORRY BUT IT'S URGENT. We've taken too long to write the details and it is now urgent. So my apologies I will be asking for designers to work quickly.

We will continue to use our existing web hosting company and url. Their is a link to the old website in the Design Brief.
Updates

UPDATE:  Please see the new file UPDATE TO DESIGN BRIEF.
Thanks for all your submissions to date.  We hope the update will assist with your designs.
As indicated in previous messages, we are happy with the Home Page + 1 Page in order to select the designer to work with in creating the full design. 

Thankyou Designers.  Much appreciate your efforts.
It's getting late here on Norfolk so I won't have much chance too review any more designs this evening.
But for your information:
Designer 7318405 Ravindra Mehta is so far the closest to what we are seeking.
Thanks again. 

Reason: Have extended to Monday 7 October to give time for designers to submit after feedback today. Especially given the time differences

Target Market(s)

Very wide audience. Current client group not that tech savvy, but we hope to broaden our market and sell more creative products, and so website needs to consider how people now use media, ie tablets & iphones.

Industry/Entity Type

Shopping

Requirements
Nice to have
• PLEASE SEE THE "UPDATE TO THE DESIGN BRIEF"

```html
<!DOCTYPE html>
<html lang="en">
<head>
<meta charset="utf-8">
<title>Bluewater Getaways KT</title>
<link href="https://fonts.googleapis.com/css2?family=Josefin+Sans:wght@300;400&family=Cormorant+Garamond:wght@500&family=Arimo:wght@400;700&display=swap" rel="stylesheet">
<style>
  :root {
    --accent-orange: #e8832a;
    --header-cream: #fff8ea;
    --brand-green: #1f8a55;
    --footer-green: #1e8754;
    --nav-white: #ffffff;
    --muted-grey: #6b6b6b;
    --sky-deep: #1e58c4;
    --sky-mid: #3d7fd6;
    --sky-glow: rgba(214, 232, 255, 0.85);
    --sea-blue: #3a85b8;
    --grass-green: #7fb23a;
    --forest-dark: rgba(28, 54, 26, 0.88);
  }
  * { margin: 0; padding: 0; box-sizing: border-box; }
  html, body { width: 1200px; height: 872px; overflow: hidden; }
  body { position: relative; font-family: "Arimo", Arial, sans-serif; background: #fff; }

  .hero-photo {
    position: absolute; left: 0; top: 56px; width: 1200px; height: 756px;
    background:
      radial-gradient(ellipse 38% 45% at 6% 6%, var(--sky-glow) 0%, rgba(214,232,255,0) 100%),
      radial-gradient(ellipse 35% 40% at 10% 82%, var(--sea-blue) 0%, rgba(58,133,184,0) 100%),
      radial-gradient(ellipse 65% 50% at 80% 100%, var(--grass-green) 0%, rgba(127,178,58,0.55) 55%, rgba(127,178,58,0) 100%),
      linear-gradient(90deg, rgba(28,54,26,0) 45%, var(--forest-dark) 82%),
      linear-gradient(180deg, var(--sky-deep) 0%, var(--sky-mid) 42%, #2f6f9e 66%, #3f7a2e 100%);
  }

  .site-header {
    position: absolute; left: 0; top: 0; width: 1200px; height: 56px;
    background: var(--header-cream); border-top: 4px solid var(--accent-orange);
  }
  .brand-name {
    position: absolute; left: 75px; top: 13px; width: 90px;
    font-size: 14px; font-weight: 700; line-height: 15px; color: var(--accent-orange);
    text-transform: uppercase;
  }
  .brand-notch {
    position: absolute; left: 512px; top: -62px; width: 164px; height: 164px;
    border-radius: 50%; background: var(--header-cream);
    display: flex; flex-direction: column; align-items: center; justify-content: flex-end;
    padding-bottom: 32px;
  }
  .brand-notch span {
    font-size: 13px; font-weight: 700; line-height: 15px; color: var(--brand-green);
    text-transform: uppercase; text-align: center;
  }
  .account-links {
    position: absolute; left: 913px; top: 20px;
    font-size: 13px; color: var(--muted-grey);
  }
  .account-links .sep { margin: 0 6px; }
  .social-links {
    position: absolute; left: 1030px; top: 20px;
    font-size: 12px; color: var(--muted-grey);
  }
  .social-links span { margin-left: 8px; }

  .main-nav a {
    position: absolute; top: 74px; font-size: 13px; color: var(--nav-white);
    text-decoration: none; text-transform: uppercase; white-space: nowrap;
  }
  .main-nav .has-menu::after { content: " ˅"; font-size: 10px; }

  .hero-title {
    position: absolute; left: 0; top: 278px; width: 1200px; text-align: center;
    font-family: "Josefin Sans", sans-serif; font-weight: 300; font-size: 50px;
    letter-spacing: 3px; color: #fff; text-transform: uppercase;
  }
  .hero-tagline {
    position: absolute; left: 0; top: 338px; width: 1200px; text-align: center;
    font-family: "Josefin Sans", sans-serif; font-weight: 300; font-size: 20px;
    letter-spacing: 1.5px; color: #fff; text-transform: uppercase;
  }
  .hero-tagline .dot { margin: 0 11px; font-size: 14px; vertical-align: 2px; }

  .about-button {
    position: absolute; left: 522px; top: 636px; width: 211px; height: 52px;
    border: 2px solid #fff; color: #fff; text-decoration: none;
    font-family: "Cormorant Garamond", serif; font-weight: 500; font-size: 24px;
    display: flex; align-items: center; justify-content: center; gap: 16px;
  }

  .site-footer {
    position: absolute; left: 0; top: 812px; width: 1200px; height: 60px;
    background: var(--footer-green); color: #fff; font-size: 13px;
  }
  .site-footer .copyright { position: absolute; left: 176px; top: 22px; }
  .site-footer .contact-email { position: absolute; left: 695px; top: 22px; display: flex; gap: 6px; align-items: center; }
  .site-footer .contact-phone { position: absolute; left: 907px; top: 22px; display: flex; gap: 6px; align-items: center; }
  .site-footer .sep { margin: 0 8px; }
</style>
</head>
<body>
  <div class="hero-photo" role="img" aria-label="Coastal headland with tall pine trees, green grassy slope and sparkling blue sea under a clear sky"></div>

  <header class="site-header">
    <div class="brand-name">Bluewater Getaways</div>
    <div class="brand-notch"><span>Bluewater<br>Getaways</span></div>
    <div class="account-links"><span>Login</span><span class="sep">|</span><span>Register</span></div>
    <div class="social-links"><span>Follow</span><span>Share</span><span>Feed</span></div>
  </header>

  <nav class="main-nav">
    <a href="#" style="left:196px">Home</a>
    <a href="#" class="has-menu" style="left:265px">Overview</a>
    <a href="#" style="left:364px">Kestrel Island</a>
    <a href="#" class="has-menu" style="left:695px">Services</a>
    <a href="#" style="left:787px">Our Shop</a>
    <a href="#" style="left:882px">Make a Booking</a>
    <a href="#" style="left:1018px">Testimonials</a>
  </nav>

  <h1 class="hero-title">Bluewater Getaways</h1>
  <p class="hero-tagline">Diversity<span class="dot">●</span>Caring<span class="dot">●</span>Community<span class="dot">●</span>Kestrel Island</p>

  <a href="#" class="about-button">About Us
    <svg width="26" height="14" viewBox="0 0 26 14"><polyline points="1,1 13,13 25,1" fill="none" stroke="#fff" stroke-width="1.5"/></svg>
  </a>

  <footer class="site-footer">
    <div class="copyright">Copyright © 2013 Bluewatergetaways</div>
    <div class="contact-email">
      <svg width="16" height="11" viewBox="0 0 16 11"><rect x="0.5" y="0.5" width="15" height="10" fill="#fff"/><polyline points="0.5,0.5 8,6 15.5,0.5" fill="none" stroke="#1e8754" stroke-width="1"/></svg>
      hello@bluewatergetaways.org
    </div>
    <div class="contact-phone">
      <svg width="14" height="11" viewBox="0 0 14 11"><path d="M1 4 Q7 -1 13 4 L11 5 L9 3.5 L5 3.5 L3 5 Z" fill="#fff"/><rect x="3" y="6" width="8" height="5" rx="1" fill="#fff"/></svg>
      +67 23 51894<span class="sep">|</span>800 614 382
    </div>
  </footer>
</body>
</html>
```